Retail Flooring Business Monthly Flyer

I need a flyer design for a retail flooring buiness based in North Vancouver, BC that caters to the lower mainland market place.

The company sales & installs all type of flooring.(hardwood, laminate, carpet, tile, epoxy flooring) as well as small renovations (kitchens, & bathroom renovations). Our current logo is blue red & white and can be seen on the following website: www.larchvalecovering.example

I would like to create a flyer that will target a mid to high end customer base. The flyer should also carry our monthly specials. We want to use the same logo.

The flyer should be simple, clean, & modern. We are open to all of your creativity.

Target Market(s)

30-65 years old homeowners mid to high end

Industry/Entity Type

Retail

Requirements
Must have
• Must have:
- Monthly specials
- Current Logo
Specials:
- Wide Plank Oak $6.49
- Brushed Oak $5.99
- Canadian Maple (4 colours) $6.49
- Asian Maple ( 1 colour left) $4.49
- Royal Sapele $6.29
- Natural Jatoba $6.29
- Bamboo Click (2 colours left) $4.99
- Bamboo T&G (1 colour left) $4.49

```html
<!DOCTYPE html>
<html lang="en">
<head>
<meta charset="utf-8">
<title>Larchvale Covering – Monthly Flyer</title>
<link rel="stylesheet" href="https://fonts.googleapis.com/css2?family=Lato:wght@300;400;700&family=Roboto+Condensed:ital,wght@0,400;0,700;1,700&display=swap">
<style>
  :root {
    --canvas: #000000;
    --red: #c1283c;
    --red-deep: #9c1f3a;
    --red-wine: #7e1a36;
    --red-light: #d44a5e;
    --band: #d0344a;
    --white: #ffffff;
    --logo-ink: #2b2876;
    --logo-mark: #d4232f;
    --panel: rgba(255,255,255,0.88);
  }
  * { margin: 0; padding: 0; box-sizing: border-box; }
  html, body { width: 1200px; height: 832px; overflow: hidden; background: var(--canvas); }
  .canvas { position: relative; width: 1200px; height: 832px; background: var(--canvas); }

  .page { position: absolute; top: 46px; width: 486px; height: 750px; overflow: hidden; background: var(--red); }
  .page--front { left: 96px; }
  .page--specials { left: 619px; }
  .page__shapes { position: absolute; inset: 0; }

  .brand {
    position: absolute; display: flex; align-items: center; gap: 10px;
    background: var(--panel); border-radius: 0 8px 8px 0;
    font-family: "Lato", sans-serif; font-weight: 400; color: var(--logo-ink);
  }
  .brand__square { width: 18px; height: 18px; background: var(--logo-mark); }
  .page--front .brand { left: 0; top: 16px; width: 354px; height: 62px; padding-left: 24px; font-size: 25px; letter-spacing: 3px; }
  .page--specials .brand { right: 0; top: 22px; width: 244px; height: 42px; padding-left: 16px; font-size: 16px; letter-spacing: 2px; border-radius: 6px 0 0 6px; }

  .photo-circle {
    position: absolute; border-radius: 50%;
    border: 6px solid rgba(255,255,255,0.55);
  }
  .page--front .photo-circle { left: 317px; top: 334px; width: 138px; height: 138px;
    background: radial-gradient(circle at 55% 40%, #e8dccb 0%, #b98a52 55%, #8a5a2c 100%); }
  .page--specials .photo-circle { left: 286px; top: 538px; width: 162px; height: 162px;
    background: radial-gradient(circle at 50% 45%, #f2f0ea 0%, #d8d2c4 55%, #8b8a6e 100%); }

  .service-list { position: absolute; left: 18px; top: 484px; list-style: none; font-family: "Lato", sans-serif; }
  .service-list li { display: flex; align-items: center; height: 35px; }
  .service-list .num {
    width: 22px; height: 22px; border: 1.5px solid var(--white); border-radius: 50%;
    color: var(--white); font-size: 14px; font-weight: 700; display: flex; align-items: center; justify-content: center;
  }
  .service-list .label {
    margin-left: 12px; width: 166px; color: var(--white); font-size: 19px; font-weight: 400;
    border-bottom: 1px solid var(--white); line-height: 22px;
  }

  .extras { position: absolute; left: 250px; top: 514px; width: 222px; list-style: none; text-align: center; font-family: "Lato", sans-serif; }
  .extras li { color: rgba(255,255,255,0.88); font-size: 16px; font-weight: 300; letter-spacing: 0.3px; height: 37px; line-height: 22px; position: relative; }
  .extras li + li::before {
    content: ""; position: absolute; left: 26px; right: 26px; top: -8px; height: 1px; background: rgba(90,10,30,0.6);
  }
  .extras li + li::after {
    content: ""; position: absolute; left: 50%; top: -10px; width: 5px; height: 5px; margin-left: -2px;
    background: rgba(90,10,30,0.8); transform: rotate(45deg);
  }

  .address { position: absolute; left: 0; right: 0; top: 690px; text-align: center; font-family: "Lato", sans-serif; font-size: 13px; color: rgba(255,255,255,0.85); }
  .footer-band { position: absolute; left: 0; right: 0; top: 711px; height: 24px; background: var(--band);
    text-align: center; font-family: "Lato", sans-serif; font-weight: 700; font-size: 18px; letter-spacing: 4px; color: var(--white); line-height: 24px; }
  .page--specials .footer-band { top: 710px; font-weight: 400; font-size: 13px; letter-spacing: 3px; text-align: left; padding-left: 18px; }

  .specials-title { position: absolute; left: 26px; top: 302px; }
  .specials-title__text { position: absolute; left: 86px; top: 6px; font-family: "Roboto Condensed", sans-serif; font-style: italic; font-weight: 700; font-size: 22px; color: var(--white); }

  .specials-grid { position: absolute; left: 25px; top: 354px; display: flex; font-family: "Roboto Condensed", sans-serif; color: var(--white); }
  .specials-col { width: 137px; height: 198px; padding-top: 1px; }
  .specials-col + .specials-col { border-left: 1px solid rgba(255,255,255,0.8); padding-left: 23px; }
  .specials-col:first-child { width: 113px; }
  .item { height: 72px; }
  .specials-col:first-child .item:nth-child(2) { height: 64px; }
  .item__name { font-size: 14px; line-height: 16px; }
  .item__note { font-size: 14px; font-weight: 700; line-height: 16px; }
  .item__price { font-size: 21px; font-weight: 700; line-height: 24px; }
</style>
</head>
<body>
<div class="canvas">

  <!-- Front page -->
  <section class="page page--front">
    <svg class="page__shapes" width="486" height="750" viewBox="0 0 486 750">
      <defs>
        <linearGradient id="kitchenTone" x1="0" y1="0" x2="0" y2="1">
          <stop offset="0" stop-color="#eeeae2"/>
          <stop offset="0.45" stop-color="#c99a68"/>
          <stop offset="1" stop-color="#a26a3c"/>
        </linearGradient>
      </defs>
      <rect x="0" y="0" width="486" height="460" fill="url(#kitchenTone)" role="img" aria-label="Photo of a modern kitchen with wood cabinets and hardwood floor"/>
      <path d="M0,352 C110,330 230,345 310,400 C350,428 395,420 420,360 C450,280 440,120 470,0 L486,0 L486,750 L0,750 Z" fill="var(--red-wine)"/>
      <path d="M0,380 C120,350 240,375 320,430 C370,462 412,440 432,370 C455,290 462,140 486,40 L486,750 L0,750 Z" fill="var(--red-deep)"/>
      <path d="M0,412 C120,380 250,410 330,462 C380,492 420,470 445,400 C465,330 475,200 486,130 L486,750 L0,750 Z" fill="var(--red)"/>
    </svg>
    <div class="brand"><span class="brand__square"></span>larchvalecovering</div>
    <div class="photo-circle" role="img" aria-label="Photo of a wooden staircase in a bright hallway"></div>

    <ol class="service-list">
      <li><span class="num">1</span><span class="label">HARDWOOD</span></li>
      <li><span class="num">2</span><span class="label">LAMINATE</span></li>
      <li><span class="num">3</span><span class="label">CARPET</span></li>
      <li><span class="num">4</span><span class="label">TILE</span></li>
      <li><span class="num">5</span><span class="label">EPOXY FLOORING</span></li>
    </ol>
    <ul class="extras">
      <li>KITCHENS CABINETS</li>
      <li>GARAGE REMODELING</li>
      <li>EPOXY FLOOR COVERING</li>
      <li>FLOORING INSTALLATION</li>
    </ul>

    <p class="address">2280 Harlow Street, North Vancouver, B.C. V7P 0A0</p>
    <p class="footer-band">Tel: 604-555-0148</p>
  </section>

  <!-- Specials page -->
  <section class="page page--specials">
    <svg class="page__shapes" width="486" height="750" viewBox="0 0 486 750">
      <defs>
        <linearGradient id="roomTone" x1="0" y1="0" x2="0" y2="1">
          <stop offset="0" stop-color="#d9c7a6"/>
          <stop offset="0.3" stop-color="#8a4a2a"/>
          <stop offset="1" stop-color="#6e3218"/>
        </linearGradient>
      </defs>
      <rect x="0" y="0" width="486" height="640" fill="url(#roomTone)" role="img" aria-label="Photo of a leather armchair on a rich hardwood floor by a window"/>
      <path d="M0,0 L300,0 C200,8 130,28 60,50 C30,58 12,60 0,60 Z" fill="var(--red-deep)"/>
      <path d="M0,0 L240,0 C160,10 90,30 0,40 Z" fill="var(--red)"/>
      <path d="M486,240 C470,330 462,460 466,560 L486,560 Z" fill="var(--red-deep)"/>
      <path d="M0,575 C110,560 230,600 300,660 C360,700 420,690 470,600 L486,560 L486,750 L0,750 Z" fill="var(--red-wine)"/>
      <path d="M0,600 C120,585 240,630 310,690 C360,720 420,720 486,650 L486,750 L0,750 Z" fill="var(--red)"/>
    </svg>
    <div class="brand"><span class="brand__square"></span>larchvalecovering</div>

    <div class="specials-title">
      <svg width="206" height="38" viewBox="0 0 206 38">
        <path d="M0,10 L200,0 L206,30 L190,36 L6,36 Z" fill="var(--red)"/>
        <rect x="22" y="9" width="20" height="20" fill="var(--white)"/>
      </svg>
      <span class="specials-title__text">SPECIALS:</span>
    </div>

    <div class="specials-grid">
      <div class="specials-col">
        <div class="item"><p class="item__name">Wide Plank Oak</p><p class="item__price">$6.49</p></div>
        <div class="item"><p class="item__name">Brushed Oak</p><p class="item__price">$5.99</p></div>
        <div class="item"><p class="item__name">Canadian Maple</p><p class="item__note">(4 Colors)</p><p class="item__price">$6.49</p></div>
      </div>
      <div class="specials-col">
        <div class="item"><p class="item__name">Natural Jatoba</p><p class="item__price">$6.29</p></div>
        <div class="item"><p class="item__name">Royal Sapele</p><p class="item__price">$6.29</p></div>
        <div class="item"><p class="item__name">Asian Maple</p><p class="item__note">(1 Colors left)</p><p class="item__price">$4.49</p></div>
      </div>
      <div class="specials-col">
        <div class="item"><p class="item__name">Bamboo Click</p><p class="item__note">(2 Colors left)</p><p class="item__price">$4.99</p></div>
        <div class="item"><p class="item__name">Bamboo T&amp;G</p><p class="item__note">(1 Colors left)</p><p class="item__price">$4.49</p></div>
      </div>
    </div>

    <div class="photo-circle" role="img" aria-label="Photo of a bright living room with a stone fireplace and rug"></div>
    <p class="footer-band">www.larchvalecovering.example</p>
  </section>

</div>
</body>
</html>
```